Business Card for Multi-Brand Sportswear Company

We are looking for a business card which represents our company and the multiple brands within it.

The company: Kelt Athletic (LTD)
The brands: Kelt, PawaLuni, VerdantFlex, Grit and Gale

Employees using these cards would be representing Kelt Athletic, rather than any of the individual brands. You will see a current design within the uploaded files, to give some inspiration. The actual text of the brands is not necessary, but the logos should be on there is some format.

Our creative minds on this are stretched, so we are looking for someone to make this their own, and show us what a good business card should look like.

We may like to get these printed with spot gloss, so keep that in mind with your designs.

www.keltathletic.co.uk

Industry/Entity Type

Business

Contact Information for Business Card

Tom Hollingsworth-Pryce
Operations Manager
(+44) 1632 960 418
Tom@keltathletic.co.uk
www.keltathletic.co.uk

Font styles to use
Sans Serif
Other font styles liked:
• Eurostile

Colors
ffffff

Requirements
Nice to have
• Dark (black) background

```html
<!DOCTYPE html>
<html lang="en">
<head>
<meta charset="utf-8">
<title>Kelt Athletic – Business Card</title>
<link rel="stylesheet" href="https://fonts.googleapis.com/css2?family=Saira:wght@400;500;700&display=swap">
<style>
  :root{
    --stage:#4a4948;
    --red:#e31e26;
    --red-deep:#c8171f;
    --black:#050505;
    --white:#ffffff;
    --paper:#f1f1f1;
    --ink:#151515;
    --violet:#4b3d5c;
    --font:"Saira", sans-serif;
  }
  *{box-sizing:border-box;margin:0;padding:0}
  html,body{width:1200px;height:960px;overflow:hidden}
  body{background:var(--stage);font-family:var(--font);position:relative}

  .card{position:absolute;left:280px;width:640px;height:414px;overflow:hidden;border-radius:4px}
  .card--back{top:44px;background:var(--black)}
  .card--front{top:502px;background:linear-gradient(135deg,var(--paper),var(--white) 55%)}

  /* back */
  .back-band{position:absolute;left:0;top:0;width:100%;height:190px;background:var(--red-deep)}
  .back-pill{position:absolute;left:140px;top:140px;width:360px;height:100px;border-radius:50px;
    background:var(--paper);display:flex;flex-direction:column;align-items:center;justify-content:center;gap:2px}
  .wordmark{display:flex;align-items:center;gap:10px}
  .wordmark__dot{width:14px;height:14px;border-radius:50%;background:var(--red)}
  .wordmark__name{font-weight:700;font-size:34px;color:var(--ink);line-height:1}
  .tagline{font-weight:500;font-size:11px;letter-spacing:3px;color:var(--ink)}

  /* front */
  .front-red-base{position:absolute;left:0;top:257px;width:100%;height:157px;background:var(--red)}
  .front-red-side{position:absolute;left:330px;top:120px;width:310px;height:160px;background:var(--red)}
  .name-panel{position:absolute;left:310px;top:70px;width:290px;height:160px;border-radius:30px;background:var(--white)}
  .front-brand{position:absolute;left:44px;top:112px}
  .front-brand .wordmark__name{font-size:32px}
  .front-brand .tagline{margin-top:4px;padding-left:24px;font-size:10px}

  .person{position:absolute;left:334px;top:142px}
  .person__name{font-size:28px;font-weight:400;color:var(--ink);line-height:1}
  .person__first{font-weight:700;color:var(--red)}
  .person__role{font-size:18px;color:var(--ink);margin-top:4px}

  .contact{position:absolute;left:40px;top:292px;list-style:none;color:var(--white);font-size:16px}
  .contact li{display:flex;align-items:center;gap:12px;height:30px}
  .contact svg{width:14px;height:14px;flex:none}

  .brands{position:absolute;left:300px;top:298px;width:320px;height:40px;border-radius:20px;background:var(--white);
    display:flex;align-items:center;justify-content:space-around;padding:0 12px}
  .brands span{font-size:11px;font-weight:700}
  .brand--pawaluni{color:var(--violet)}
  .brand--grit{color:var(--red)}
  .brand--kelt{color:var(--ink)}
  .brand--verdant{color:var(--red)}
</style>
</head>
<body>

<section class="card card--back" aria-label="Card back">
  <div class="back-band"></div>
  <div class="back-pill">
    <div class="wordmark"><span class="wordmark__dot"></span><span class="wordmark__name">Kelt Athletic</span></div>
    <div class="tagline">PERFORMANCE WEAR</div>
  </div>
</section>

<section class="card card--front" aria-label="Card front">
  <div class="front-red-base"></div>
  <div class="front-red-side"></div>
  <div class="name-panel"></div>

  <div class="front-brand">
    <div class="wordmark"><span class="wordmark__dot"></span><span class="wordmark__name">Kelt Athletic</span></div>
    <div class="tagline">PERFORMANCE WEAR</div>
  </div>

  <div class="person">
    <div class="person__name"><span class="person__first">Rhys</span> Calder</div>
    <div class="person__role">Managing Director</div>
  </div>

  <ul class="contact">
    <li>
      <svg viewBox="0 0 16 16" aria-hidden="true"><path fill="#fff" d="M3.5 1l2.5 3-1.5 1.5c.8 2 2.2 3.4 4 4.2L10 8.2l3 2.5-1 3c-6 .3-11-4.7-10.5-10.7z"/></svg>
      +44 (0)1632 960418
    </li>
    <li>
      <svg viewBox="0 0 16 16" aria-hidden="true"><rect x="1.5" y="3.5" width="13" height="9" fill="none" stroke="#fff" stroke-width="1.5"/><path d="M1.5 3.5l6.5 5 6.5-5" fill="none" stroke="#fff" stroke-width="1.5"/></svg>
      rhys@keltathletic.co.uk
    </li>
    <li>
      <svg viewBox="0 0 16 16" aria-hidden="true"><circle cx="8" cy="8" r="6.5" fill="none" stroke="#fff" stroke-width="1.4"/><ellipse cx="8" cy="8" rx="2.8" ry="6.5" fill="none" stroke="#fff" stroke-width="1.2"/><path d="M1.5 8h13" stroke="#fff" stroke-width="1.2"/></svg>
      www.keltathletic.co.uk
    </li>
  </ul>

  <div class="brands" aria-label="Group brands">
    <span class="brand--pawaluni">PawaLuni</span>
    <span class="brand--grit">Grit and Gale</span>
    <span class="brand--kelt">Kelt</span>
    <span class="brand--verdant">VerdantFlex</span>
  </div>
</section>

</body>
</html>
```